Trendy eye catching business card for lawn mowing business

Verge Kings, a local community lawn mowing service, requires an eye catching trendy business card to drop into letterboxes.

We could simply throw something together from a Microsoft Word template, but we are wanting something more than this. Some other business’ images are attached for some inspiration.

We are requiring the card to have Verge Kings with our slogan, Call The Pembrys. In addition, provide details with that we are a local, affordable lawn mowing service, and for other gardening matters to simply just ask!
Plus the relevant contact details, phone, email, social media.

Target Market(s)

Local community members who require assistance with their garden care

Industry/Entity Type

Gardening

Contact Information for Business Card

the name VERGE KINGS is our logo
telephone logo 0438 215 967
email logo vergekings@postbox-demo.com
Instagram logo vergekings
Facebook logo vergekings.sth
Lawn Mowing Service
Local Affordable
edge trim, blow and clipping removal included.
Other gardening matters, just ask!

Font styles to use
Serif
Sans Serif
Decorative
Script

Colors
9bcb3c
ffffff

Requirements
Must have
• All the details listed in Business Card Details.
Make these words prominent:
Verge Kings
Lawn Mowing Service
Local
Affordable
Nice to have
• Our slogan ‘Call The Pembrys’ incorporated.
Different colour background for front and reverse side
Greens, white and black colours
Subtle grass blades images incorporated
Should not have
• No images of lawnmowers.
No images of men/cartoons.
No using initials for Verge Kings

```html
<!DOCTYPE html>
<html lang="en">
<head>
<meta charset="utf-8">
<title>Verge Kings Business Card</title>
<link rel="stylesheet" href="https://fonts.googleapis.com/css2?family=Poppins:wght@400;600;800&family=Dancing+Script:wght@500&display=swap">
<style>
  :root {
    --backdrop: #9a9a9c;
    --card-light: #e4eedf;
    --green-deep: #0f6a1a;
    --green-mid: #2c9a2c;
    --green-bright: #5cc53c;
    --green-accent: #9bcb3c;
    --ink-green: #1d6a22;
    --text-grey: #4a5a4a;
    --text-dark: #0d3f12;
    --white: #ffffff;
  }
  * { box-sizing: border-box; margin: 0; padding: 0; }
  html, body { width: 1200px; height: 801px; overflow: hidden; }
  body {
    background: var(--backdrop);
    font-family: "Poppins", sans-serif;
    position: relative;
  }
  .card {
    position: absolute;
    top: 240px;
    width: 560px;
    height: 320px;
    border-radius: 22px;
    overflow: hidden;
    box-shadow: 0 10px 24px rgba(0,0,0,.25);
  }
  .card-front { left: 26px; background: var(--card-light); }
  .card-back {
    left: 614px;
    background: linear-gradient(180deg, var(--green-deep) 0%, #18791f 45%, var(--green-mid) 75%, var(--green-bright) 100%);
  }

  /* front */
  .brand {
    position: absolute;
    left: 46px; top: 116px;
    width: 230px;
  }
  .brand-name {
    font-weight: 800;
    font-size: 40px;
    line-height: 1;
    color: var(--ink-green);
    letter-spacing: 1px;
  }
  .brand-slogan {
    font-family: "Dancing Script", cursive;
    font-size: 30px;
    line-height: 1.2;
    color: var(--green-mid);
    margin-top: 6px;
    margin-left: 30px;
    white-space: nowrap;
  }
  .divider {
    position: absolute;
    left: 296px; top: 92px;
    width: 1px; height: 136px;
    background: var(--ink-green);
  }
  .contact {
    position: absolute;
    left: 318px; top: 98px;
  }
  .contact-name {
    font-weight: 800;
    font-size: 20px;
    color: var(--ink-green);
    margin-bottom: 10px;
    white-space: nowrap;
  }
  .contact-list { list-style: none; }
  .contact-item {
    display: flex; align-items: center; gap: 8px;
    font-size: 12.5px;
    color: var(--text-grey);
    line-height: 1.7;
    white-space: nowrap;
  }
  .contact-icon { width: 12px; height: 12px; flex: none; }

  /* back */
  .grass {
    position: absolute;
    left: 0; bottom: 0;
    width: 100%; height: 180px;
    background: linear-gradient(180deg, rgba(92,197,60,0) 0%, rgba(92,197,60,.45) 40%, rgba(92,197,60,.75) 100%);
  }
  .claims {
    position: absolute;
    left: 34px; top: 48px;
    list-style: none;
  }
  .claim {
    display: flex; align-items: center; gap: 12px;
    font-weight: 600;
    font-size: 30px;
    line-height: 1.2;
    color: var(--white);
    white-space: nowrap;
  }
  .tick { width: 28px; height: 28px; flex: none; }
  .extras {
    position: absolute;
    left: 0; right: 0; top: 176px;
    text-align: center;
    font-weight: 600;
    font-size: 15px;
    line-height: 1.35;
    color: var(--text-dark);
  }
  .phone-pill {
    position: absolute;
    left: 50%; top: 232px;
    transform: translateX(-50%);
    display: flex; align-items: center; gap: 10px;
    height: 54px;
    padding: 0 24px 0 8px;
    border-radius: 27px;
    background: var(--green-deep);
    box-shadow: inset 0 2px 4px rgba(0,0,0,.3);
    white-space: nowrap;
  }
  .phone-badge { width: 38px; height: 38px; flex: none; }
  .phone-number {
    font-weight: 800;
    font-size: 32px;
    line-height: 1;
    color: var(--green-bright);
    letter-spacing: 1px;
    white-space: nowrap;
  }
</style>
</head>
<body>

<section class="card card-front" aria-label="Card front">
  <div class="brand">
    <div class="brand-name">VERGE<br>KINGS</div>
    <div class="brand-slogan">Call The Pembrys</div>
  </div>
  <div class="divider"></div>
  <div class="contact">
    <div class="contact-name">ROWAN PEMBRY</div>
    <ul class="contact-list">
      <li class="contact-item">
        <svg class="contact-icon" viewBox="0 0 24 24"><path fill="#1d6a22" d="M6.6 10.8a15 15 0 0 0 6.6 6.6l2.2-2.2a1 1 0 0 1 1-.25 11.4 11.4 0 0 0 3.6.6 1 1 0 0 1 1 1V20a1 1 0 0 1-1 1A17 17 0 0 1 3 4a1 1 0 0 1 1-1h3.5a1 1 0 0 1 1 1c0 1.25.2 2.45.6 3.6a1 1 0 0 1-.25 1z"/></svg>
        0438 215 967
      </li>
      <li class="contact-item">
        <svg class="contact-icon" viewBox="0 0 24 24"><rect x="2" y="5" width="20" height="14" rx="2" fill="#1d6a22"/><path d="M3 6l9 7 9-7" stroke="#e4eedf" stroke-width="2" fill="none"/></svg>
        vergekings@postbox-demo.com
      </li>
      <li class="contact-item">
        <svg class="contact-icon" viewBox="0 0 24 24"><circle cx="12" cy="12" r="9" fill="#1d6a22"/></svg>
        vergekings.sth
      </li>
      <li class="contact-item">
        <svg class="contact-icon" viewBox="0 0 24 24"><circle cx="12" cy="12" r="9" fill="none" stroke="#1d6a22" stroke-width="2.5"/></svg>
        vergekings
      </li>
    </ul>
  </div>
</section>

<section class="card card-back" aria-label="Card back">
  <div class="grass" role="img" aria-label="Soft grass blades rising along the lower half of the card"></div>
  <ul class="claims">
    <li class="claim">
      <svg class="tick" viewBox="0 0 28 28"><circle cx="14" cy="14" r="13" fill="#2c9a2c"/><path d="M8 14.5l4 4 8-9" stroke="#fff" stroke-width="3" fill="none" stroke-linecap="round" stroke-linejoin="round"/></svg>
      LAWN MOWING SERVICE
    </li>
    <li class="claim">
      <svg class="tick" viewBox="0 0 28 28"><circle cx="14" cy="14" r="13" fill="#2c9a2c"/><path d="M8 14.5l4 4 8-9" stroke="#fff" stroke-width="3" fill="none" stroke-linecap="round" stroke-linejoin="round"/></svg>
      LOCAL. AFFORDABLE.
    </li>
  </ul>
  <p class="extras">Edge trim, blow &amp; clipping removal included.<br>Other gardening matters, just ask!</p>
  <div class="phone-pill">
    <svg class="phone-badge" viewBox="0 0 38 38"><circle cx="19" cy="19" r="18" fill="#5cc53c"/><circle cx="19" cy="19" r="13" fill="#fff"/><path transform="translate(11 11) scale(.68)" fill="#0f6a1a" d="M6.6 10.8a15 15 0 0 0 6.6 6.6l2.2-2.2a1 1 0 0 1 1-.25 11.4 11.4 0 0 0 3.6.6 1 1 0 0 1 1 1V20a1 1 0 0 1-1 1A17 17 0 0 1 3 4a1 1 0 0 1 1-1h3.5a1 1 0 0 1 1 1c0 1.25.2 2.45.6 3.6a1 1 0 0 1-.25 1z"/></svg>
    <span class="phone-number">0438 215 967</span>
  </div>
</section>

</body>
</html>
```